Social house sales

An app that allows someone to search for houses for sale in a certain city or post code...then returns the results and allows the user to like or comment on each property for sale, and @mention others who are users.
UPDATE:
May i know whats your apps name?and please attach the logo.
also - No logo yet! But the name is ''Pelko''
can i get more specific how many pages you want? - Five pages of the mocked up is fine
can you provide the wireframe? - I haven''t done any wire frames, looking for inspiration! Registration/opening splash page, search page, results page, comment/liking, @mentioning someone - those could be five views
and are this app have profile page? No
login with qm or brindlo or vaultspan? QM
which OS i should design it? (IOS,Android) iOS
House buyers, renters
House

```html
<!DOCTYPE html>
<html lang="en">
<head>
<meta charset="utf-8">
<title>Pelko – Sign in</title>
<link rel="stylesheet" href="https://fonts.googleapis.com/css2?family=Montserrat:wght@800&family=Roboto:wght@300;500;700&display=swap">
<style>
  :root {
    --status-bg: #000000;
    --status-fg: #ffffff;
    --grad-top: #dc5fea;
    --grad-mid: #9a72bb;
    --grad-bottom: #8667c0;
    --grad-shade: rgba(110, 90, 150, 0.45);
    --white: #ffffff;
    --field-bg: #f0f0f0;
    --field-text: #4a4a4a;
    --placeholder: #a8a8a8;
    --valid: #4fd31a;
    --button-bg: #5670ad;
    --button-bg-dark: #4d66a3;
  }
  * { box-sizing: border-box; margin: 0; padding: 0; }
  html, body { width: 683px; height: 1200px; overflow: hidden; background: #e6e6e6; }
  .screen {
    position: relative;
    width: 683px;
    height: 1200px;
    overflow: hidden;
    background:
      radial-gradient(ellipse 70% 30% at 50% 48%, var(--grad-shade), transparent 70%),
      linear-gradient(170deg, var(--grad-top) 0%, var(--grad-mid) 45%, var(--grad-bottom) 100%);
    font-family: "Roboto", Arial, sans-serif;
  }
  .status-bar {
    position: absolute; left: 0; top: 0; width: 100%; height: 47px;
    background: var(--status-bg); color: var(--status-fg);
    display: flex; align-items: center; justify-content: space-between;
    padding: 0 14px; font-weight: 700; font-size: 24px;
  }
  .status-left, .status-right { display: flex; align-items: center; gap: 10px; width: 200px; }
  .status-right { justify-content: flex-end; }
  .status-time { flex: 1; text-align: center; }
  .brand {
    position: absolute; left: 0; top: 270px; width: 100%;
    display: flex; flex-direction: column; align-items: center; gap: 40px;
  }
  .brand-mark {
    width: 156px; height: 156px; border-radius: 50%;
    border: 11px solid var(--white);
  }
  .brand-name {
    font-family: "Montserrat", Arial, sans-serif; font-weight: 800;
    font-size: 62px; letter-spacing: 1px; color: var(--white); line-height: 1;
  }
  .login-card {
    position: absolute; left: 68px; top: 649px; width: 541px; height: 377px;
    background: var(--white); border-radius: 12px;
  }
  .field {
    position: absolute; left: 42px; width: 456px; height: 82px;
    background: var(--field-bg); border-radius: 4px;
    display: flex; align-items: center; justify-content: center;
    font-weight: 300; font-size: 27px;
  }
  .field-email { top: 36px; color: var(--field-text); border-left: 4px solid var(--valid); }
  .field-password { top: 141px; color: var(--placeholder); }
  .field-check { position: absolute; right: 20px; top: 27px; }
  .social-button {
    position: absolute; left: 42px; top: 255px; width: 456px; height: 77px;
    border-radius: 4px;
    background: linear-gradient(var(--button-bg), var(--button-bg-dark));
    display: flex; align-items: center; justify-content: center; gap: 22px;
    color: var(--white); font-weight: 700; font-size: 29px;
  }
  .social-button-square { width: 48px; height: 48px; background: var(--white); border-radius: 3px; }
</style>
</head>
<body>
<main class="screen">
  <header class="status-bar">
    <div class="status-left">
      <svg width="40" height="20" viewBox="0 0 40 20" aria-hidden="true">
        <rect x="0" y="13" width="5" height="7" fill="#fff"/>
        <rect x="8" y="10" width="5" height="10" fill="#fff"/>
        <rect x="16" y="7" width="5" height="13" fill="#fff"/>
        <rect x="24" y="3" width="5" height="17" fill="#fff"/>
        <rect x="32" y="0" width="5" height="20" fill="#fff"/>
      </svg>
      <span class="status-carrier">Vela</span>
    </div>
    <div class="status-time">1:57 PM</div>
    <div class="status-right">
      <svg width="22" height="22" viewBox="0 0 22 22" aria-hidden="true">
        <circle cx="11" cy="11" r="10" fill="#fff"/>
        <path d="M11 5v6h5" stroke="#000" stroke-width="2.5" fill="none"/>
      </svg>
      <svg width="22" height="22" viewBox="0 0 22 22" aria-hidden="true">
        <path d="M21 1L1 10l9 2 2 9z" fill="#fff"/>
      </svg>
      <svg width="30" height="28" viewBox="0 0 30 28" aria-hidden="true">
        <path d="M24 8A11 11 0 1 0 25 19" stroke="#fff" stroke-width="2.5" fill="none"/>
        <path d="M20 8h7V1z" fill="#fff"/>
        <rect x="9" y="12" width="10" height="8" fill="#fff"/>
        <path d="M11 12V9a3 3 0 0 1 6 0v3" stroke="#fff" stroke-width="2" fill="none"/>
      </svg>
      <svg width="44" height="20" viewBox="0 0 44 20" aria-hidden="true">
        <rect x="1" y="1" width="38" height="18" rx="2" stroke="#fff" stroke-width="2" fill="none"/>
        <rect x="4" y="4" width="32" height="12" fill="#fff"/>
        <rect x="40" y="6" width="3" height="8" fill="#fff"/>
      </svg>
    </div>
  </header>

  <section class="brand">
    <div class="brand-mark" aria-hidden="true"></div>
    <h1 class="brand-name">PELKO</h1>
  </section>

  <form class="login-card">
    <div class="field field-email">username@mailpost.com
      <svg class="field-check" width="30" height="26" viewBox="0 0 30 26" aria-hidden="true">
        <path d="M2 13l9 9L28 3" stroke="var(--valid)" stroke-width="3" fill="none"/>
      </svg>
    </div>
    <div class="field field-password">password</div>
    <div class="social-button">
      <span class="social-button-square" aria-hidden="true"></span>
      <span>Login with QM</span>
    </div>
  </form>
</main>
</body>
</html>
```